Brochure Design: Text Messaging Service

We are looking for a brochure design for our new text messaging service. this should be a 2 page design on a 8.5x11" page
this should a clean design that catshed the eyey and features the features and benefits.
the brochure should bew designed so that we can entice our existing business clients to adopt this new service for their business.

Target Market(s)

business owner

Industry/Entity Type

Driving School

Font styles to use
Sans Serif

Colors
0692cd
33b8a4

Requirements
Must have
• pricing info, features, and screen shot on a computer. maybe also include image of your teen with cell phone.
Nice to have
• n/a
Should not have
• n/a

```html
<!DOCTYPE html>
<html lang="en">
<head>
<meta charset="utf-8">
<title>RoadReady Software – SMS Communication Module</title>
<link href="https://fonts.googleapis.com/css2?family=Lato:wght@400;700;900&display=swap" rel="stylesheet">
<style>
  :root {
    --backdrop: #d3cbb9;
    --paper: #ffffff;
    --brand-blue: #0d5aa7;
    --brand-green: #4bb84a;
    --ink: #2b2b2b;
    --photo-warm-a: #e9c9a0;
    --photo-warm-b: #8a6f58;
    --photo-cool-a: #cfd6de;
    --photo-cool-b: #5d6f85;
  }
  * { box-sizing: border-box; margin: 0; padding: 0; }
  html, body { width: 1200px; height: 871px; overflow: hidden; }
  body {
    background: var(--backdrop);
    font-family: "Lato", Arial, sans-serif;
    color: var(--ink);
  }
  .flyer {
    position: absolute;
    left: 275px; top: 15px;
    width: 650px; height: 841px;
    background: var(--paper);
    overflow: hidden;
    box-shadow: 0 6px 18px rgba(0,0,0,.18);
  }
  .flyer-shapes { position: absolute; inset: 0; }
  .brand {
    position: absolute; left: 40px; top: 110px;
    display: flex; align-items: center; gap: 9px;
  }
  .brand-dot {
    width: 28px; height: 28px; border-radius: 50%;
    background: var(--brand-blue);
  }
  .brand-name {
    font-weight: 900; font-size: 24px; color: var(--brand-blue);
    white-space: nowrap;
  }
  .brand-tagline {
    position: absolute; left: 40px; top: 146px;
    font-size: 6.5px; font-weight: 700; letter-spacing: .6px;
    color: var(--ink); text-transform: uppercase; white-space: nowrap;
  }
  .headline {
    position: absolute; left: 40px; top: 245px;
    font-weight: 900; line-height: .95; text-transform: uppercase;
  }
  .headline span { display: block; }
  .headline .line-1 { font-size: 40px; color: var(--brand-blue); }
  .headline .line-2 { font-size: 56px; color: var(--brand-green); }
  .headline .line-3 { font-size: 38px; color: var(--brand-blue); }
  .intro {
    position: absolute; left: 250px; top: 352px; width: 360px;
    font-size: 10.5px; line-height: 1.38; text-align: justify;
  }
  .body-copy {
    position: absolute; left: 40px; top: 442px; width: 570px;
    font-size: 10.5px; line-height: 1.38;
  }
  .body-copy p { margin-bottom: 8px; }
  .body-copy .closing { width: 430px; }
  .features-title {
    position: absolute; left: 40px; top: 645px;
    font-size: 22px; font-weight: 700; color: var(--brand-green);
    text-transform: uppercase; line-height: 1.2;
  }
  .feature-list {
    position: absolute; list-style: none; top: 680px;
    font-size: 11.5px; line-height: 1.35;
  }
  .feature-list li { padding-left: 12px; position: relative; }
  .feature-list li::before {
    content: ""; position: absolute; left: 0; top: 6px;
    width: 5px; height: 5px; border-radius: 50%; background: var(--brand-green);
  }
  .feature-list.col-a { left: 40px; width: 235px; }
  .feature-list.col-b { left: 290px; width: 190px; }
  .call-us {
    position: absolute; left: 503px; top: 628px; width: 145px;
    color: #fff; text-transform: uppercase; white-space: nowrap;
  }
  .call-us .label { font-size: 28px; font-weight: 700; display: block; line-height: 1.1; }
  .call-us .phone { font-size: 23px; font-weight: 700; color: var(--brand-blue); display: block; line-height: 1.2; }
  .call-us .email { font-size: 9px; font-weight: 700; display: block; margin-top: 4px; }
</style>
</head>
<body>
<article class="flyer">
  <svg class="flyer-shapes" width="650" height="841" viewBox="0 0 650 841">
    <defs>
      <linearGradient id="hero-tone" x1="0" y1="0" x2="1" y2="1">
        <stop offset="0" stop-color="var(--photo-warm-b)"/>
        <stop offset=".55" stop-color="var(--photo-warm-a)"/>
        <stop offset="1" stop-color="var(--photo-cool-a)"/>
      </linearGradient>
      <linearGradient id="portrait-tone" x1="0" y1="0" x2="1" y2="1">
        <stop offset="0" stop-color="var(--photo-cool-b)"/>
        <stop offset="1" stop-color="var(--photo-warm-a)"/>
      </linearGradient>
    </defs>
    <path d="M285,0 H650 V215 C545,240 420,235 355,185 C310,145 285,75 285,0 Z" fill="var(--brand-green)"/>
    <path d="M300,0 H650 V203 C545,228 425,223 365,175 C322,138 300,72 300,0 Z"
          fill="url(#hero-tone)" role="img" aria-label="Photo: smiling family driving together in a car"/>
    <path d="M0,250 C110,190 250,170 380,190 C250,185 120,215 0,265 Z" fill="var(--brand-blue)"/>
    <circle cx="430" cy="272" r="68" fill="var(--brand-blue)"/>
    <circle cx="430" cy="272" r="62" fill="var(--brand-green)"/>
    <circle cx="430" cy="272" r="58" fill="url(#portrait-tone)" role="img" aria-label="Photo: teen holding new car keys"/>
    <circle cx="582" cy="228" r="52" fill="var(--brand-blue)"/>
    <circle cx="582" cy="228" r="46" fill="var(--brand-green)"/>
    <circle cx="582" cy="228" r="42" fill="url(#portrait-tone)" role="img" aria-label="Photo: young driver behind the wheel"/>
    <path d="M0,815 C220,800 430,790 650,768 V841 H0 Z" fill="var(--brand-blue)"/>
    <circle cx="612" cy="680" r="125" fill="var(--brand-green)"/>
  </svg>

  <div class="brand"><span class="brand-dot"></span><span class="brand-name">RoadReady Software</span></div>
  <div class="brand-tagline">Enrollment · Billing · Scheduling · Reporting and more</div>

  <h1 class="headline">
    <span class="line-1">We Make</span>
    <span class="line-2">Driving</span>
    <span class="line-3">Easy</span>
  </h1>

  <p class="intro">SMS Communication Module is designed to allow your school to effectively communicate with both parent and students in near real-time. In today's world, both students and parent expect almost instant communication with the service provider and driving schools.</p>

  <div class="body-copy">
    <p>With our integrated SMS Messaging Module, you're your school can automatically send reminders for classroom, in-car lessons, road tests, urgent notifications and more. Students and parent can also reply to those messages.</p>
    <p>Each school will be assigned a dedicated phone number, which could be either local number of your choice or toll-free number. Since this module is fully integrated the staff will not need to use any external or third party services to accomplish the same effect, hence saving time and money.</p>
    <p>Each SMS phone number is tracked individually and assigned to student account. During the enrollment process students and parents can opt to receive SMS notifications. However, at any point later on they can add or remove phone numbers for notifications.</p>
    <p class="closing">SMS Module is the first step in a very extensive list of features and capabilities that will be brought to to you. With plans starting at $25 / month, it is a very affordable solution for your school and business, while providing an efficient and cost effective communication tool.</p>
  </div>

  <h2 class="features-title">Features:</h2>
  <ul class="feature-list col-a">
    <li>Dedicated local or toll-free phone number</li>
    <li>Custom message content</li>
    <li>Delivery confirmation</li>
    <li>Two-way messaging</li>
  </ul>
  <ul class="feature-list col-b">
    <li>On-Demand messaging</li>
    <li>Phone number validation</li>
    <li>Online enrollment integration</li>
    <li>Mass communication</li>
    <li>Plans starting at $25 / month for 500 messages</li>
  </ul>

  <div class="call-us">
    <span class="label">Call us:</span>
    <span class="phone">123 456 7890</span>
    <span class="email">Email: lorem@lorem ipsum</span>
  </div>
</article>
</body>
</html>
```